Modern and Improved business card design for Family Dental Practice

We have 2 sets of logo we have designed and now just need a business card layout and design for the office. Colors are on the logo. We can choose which logo we want to go with . The font can be changed to whatever seems modern and relevant. We are family dental office that has been open for over 15 years in South Austin Texas.

Target Market(s)

Handout Business cards to referrals and specialists

Industry/Entity Type

Dental

Contact Information for Business Card

We need address, phone, website and email address. 4870 North Loop Rd Suite 208 , Austin,Texas 78651....phone: 512-480-7319.....email- info@maplebrookdental-example.com....website - MapleBrookDental-example.com

Font styles to use
Serif
Decorative

Requirements
Must have
• my logo. We have 2 logos, but we can use just one or if we can incorporate one on one side and the other on the other side.
Nice to have
• Really just need a modern look and clean that incorporates the logo and colors .

```html
<!DOCTYPE html>
<html lang="en">
<head>
<meta charset="utf-8">
<title>Maple Brook Family Dentistry – Business Card</title>
<link rel="stylesheet" href="https://fonts.googleapis.com/css2?family=Noto+Sans:ital,wght@0,400;0,700;1,400&display=swap">
<style>
  :root {
    --backdrop: #8e8e8e;
    --card: #ffffff;
    --ink: #222222;
    --ink-soft: #3a3a3a;
    --green: #0b6a12;
    --green-dark: #0a5a10;
    --dots: #6f6f6f;
  }
  * { margin: 0; padding: 0; box-sizing: border-box; }
  html, body { width: 1200px; height: 1200px; overflow: hidden; }
  body {
    background: var(--backdrop);
    font-family: "Noto Sans", Verdana, sans-serif;
    color: var(--ink);
    position: relative;
  }
  .card {
    position: absolute;
    left: 281px;
    width: 639px;
    height: 366px;
    background: var(--card);
    border-radius: 22px;
    overflow: hidden;
  }
  .card--front { top: 195px; }
  .card--back { top: 639px; }

  /* Brand wordmark */
  .wordmark { position: absolute; color: var(--ink); font-weight: 400; }
  .wordmark__name { display: block; font-size: 36px; line-height: 38px; letter-spacing: 0.5px; }
  .wordmark__tag { display: block; font-size: 14px; letter-spacing: 1px; margin-top: 10px; }
  .card--front .wordmark { left: 41px; top: 40px; }
  .card--back .wordmark { left: 170px; top: 55px; }
  .card--back .wordmark__name { font-size: 32px; line-height: 33px; }
  .wordmark__dot {
    position: absolute; left: -76px; top: 12px;
    width: 56px; height: 56px; border-radius: 50%;
    background: var(--green);
  }

  /* Front: person + contacts */
  .person { position: absolute; left: 42px; top: 168px; }
  .person__name { font-size: 27px; font-weight: 700; color: var(--ink-soft); letter-spacing: 1.5px; line-height: 32px; }
  .person__title { font-size: 16px; color: var(--green); letter-spacing: 0.4px; margin-top: 1px; }

  .contacts { position: absolute; left: 41px; top: 237px; list-style: none; font-size: 15px; color: var(--ink-soft); letter-spacing: 0.4px; }
  .contacts li { display: flex; align-items: flex-start; line-height: 20px; }
  .contacts svg { width: 14px; height: 14px; margin: 3px 10px 0 0; flex: none; fill: var(--green); }

  /* Back: appointment form */
  .form { position: absolute; left: 56px; right: 54px; top: 180px; }
  .form__row { display: flex; align-items: baseline; font-size: 14.5px; font-weight: 700; color: var(--green-dark); letter-spacing: 0.8px; margin-bottom: 17px; }
  .form__line { flex: 1; border-bottom: 1.5px dotted var(--dots); margin: 0 1px; transform: translateY(-3px); }
  .form__unit { font-size: 11px; letter-spacing: 0.5px; }

  .days { position: absolute; left: 70px; right: 62px; top: 262px; display: flex; justify-content: space-between; font-size: 15px; font-weight: 700; color: var(--ink-soft); letter-spacing: 1px; }
  .days span { display: flex; align-items: center; }
  .days span::before {
    content: ""; width: 12px; height: 12px; border: 1.6px solid var(--green-dark);
    margin-right: 6px;
  }

  .notice { position: absolute; left: 0; right: 0; top: 314px; text-align: center; font-size: 11.5px; font-style: italic; color: var(--ink-soft); line-height: 14px; letter-spacing: 0.3px; }
</style>
</head>
<body>

<section class="card card--front" aria-label="Business card front">
  <div class="wordmark">
    <span class="wordmark__name">MAPLE<br>BROOK</span>
    <span class="wordmark__tag">FAMILY DENTISTRY</span>
  </div>

  <div class="person">
    <p class="person__name">YOUR NAME</p>
    <p class="person__title">Dr Your Title</p>
  </div>

  <ul class="contacts">
    <li><svg viewBox="0 0 24 24"><path d="M6.6 10.8a15.1 15.1 0 0 0 6.6 6.6l2.2-2.2c.3-.3.7-.4 1-.2 1.1.4 2.3.6 3.6.6.6 0 1 .4 1 1V20c0 .6-.4 1-1 1A17 17 0 0 1 3 4c0-.6.4-1 1-1h3.5c.6 0 1 .4 1 1 0 1.3.2 2.5.6 3.6.1.3 0 .7-.2 1z"/></svg>512-480-7319</li>
    <li><svg viewBox="0 0 24 24"><path d="M2 5h20v14H2z M4 7l8 6 8-6" fill="var(--green)"/><path d="M4 7.5l8 6 8-6" fill="none" stroke="#fff" stroke-width="1.6"/></svg>info@maplebrookdental-example.com</li>
    <li><svg viewBox="0 0 24 24"><circle cx="12" cy="12" r="10"/><path d="M7 6c2 1 3 3 2 5s1 3 2 4M15 4c-1 2 0 4 2 4s3 2 3 3M13 20c0-2 1-3 3-4" fill="none" stroke="#fff" stroke-width="1.6"/></svg>MapleBrookDental-example.com</li>
    <li><svg viewBox="0 0 24 24"><path d="M12 2a7 7 0 0 0-7 7c0 5 7 13 7 13s7-8 7-13a7 7 0 0 0-7-7zm0 9.5A2.5 2.5 0 1 1 12 6.5a2.5 2.5 0 0 1 0 5z"/></svg><span>4870 North Loop Rd Suite 208<br>Austin,Texas 78651</span></li>
  </ul>
</section>

<section class="card card--back" aria-label="Business card back">
  <div class="wordmark">
    <span class="wordmark__dot" aria-hidden="true"></span>
    <span class="wordmark__name">MAPLE<br>BROOK</span>
    <span class="wordmark__tag">FAMILY DENTISTRY</span>
  </div>

  <div class="form">
    <div class="form__row">NAME<span class="form__line"></span></div>
    <div class="form__row">DATE<span class="form__line"></span>TIME<span class="form__line"></span><span class="form__unit">AM\PM</span></div>
  </div>

  <div class="days">
    <span>MON</span><span>TUES</span><span>WED</span><span>THU</span><span>FRI</span><span>SAT</span>
  </div>

  <p class="notice">If you are unable to keep your appointment, please call us to<br>rescheduleatleast 48 hours prior to your appointment.</p>
</section>

</body>
</html>
```